Property maintenance company needs an eye catching postcard design

We are a property maintenance company that wants to send out a postcard targeting residential homeowners only. We want the postcard to create the impression of a friendly and inviting company that makes maintenance easy for homeowners. I have attached all the instructions in a pdf file as well as any other needed pictures or info. Please read the outline I provided. I also attached pictures/screenshots of our new (in progress) website if you wish to get a feel for our company.

Thanks!

Target Market(s)

residential homeowners, homeowners

Industry/Entity Type

Property Maintenance

```html
<!DOCTYPE html>
<html lang="en">
<head>
<meta charset="utf-8">
<title>BrightPath Postcard</title>
<link href="https://fonts.googleapis.com/css2?family=Roboto+Condensed:wght@400;700;900&family=Open+Sans:wght@400;600;700&display=swap" rel="stylesheet">
<style>
:root{
  --navy:#14285a;
  --green:#6ab023;
  --green-dark:#4e8c17;
  --gold:#f2b51b;
  --grey-bg:#e9e9e9;
  --text-grey:#555;
  --white:#fff;
}
*{box-sizing:border-box;margin:0;padding:0}
html,body{width:849px;height:1200px;overflow:hidden;background:var(--grey-bg);font-family:"Open Sans",sans-serif}
.sheet{position:relative;width:849px;height:1200px}
.card{position:absolute;left:24px;width:801px;background:var(--white);overflow:hidden;box-shadow:0 2px 6px rgba(0,0,0,.18)}
.card--front{top:22px;height:494px}
.card--back{top:645px;height:481px}
.side-label{position:absolute;left:0;width:849px;text-align:center;font-family:"Open Sans",sans-serif;font-size:15px;letter-spacing:1px;color:#333}
.bg-art{position:absolute;inset:0}
.brand{position:absolute;display:flex;align-items:center;gap:8px}
.brand__mark{width:26px;height:26px;background:var(--navy);border-radius:4px}
.brand__name{font-family:"Roboto Condensed",sans-serif;font-weight:900;font-size:30px;color:var(--navy);line-height:1}
.brand__tag{font-family:"Roboto Condensed",sans-serif;font-weight:700;font-size:10px;letter-spacing:3px;color:var(--green);margin-left:34px;margin-top:2px}
.headline{position:absolute;left:22px;top:112px;font-family:"Roboto Condensed",sans-serif;font-weight:900;font-size:50px;line-height:.98;color:var(--navy);text-transform:uppercase}
.subline{position:absolute;left:22px;top:328px;font-family:"Roboto Condensed",sans-serif;font-weight:700;font-size:21px;line-height:1.2;color:var(--green)}
.seal{position:absolute;border-radius:50%;background:var(--gold);border:6px solid var(--navy);box-shadow:0 0 0 3px var(--gold)}
.cta-box{position:absolute;background:var(--green);color:var(--white);font-family:"Roboto Condensed",sans-serif}
.cta-box small{display:block;font-size:11px;font-weight:700}
.cta-box strong{display:block;font-size:21px;font-weight:900;line-height:1.05}
.phone-bar{position:absolute;background:var(--navy);color:var(--white);display:flex;align-items:center;gap:12px;font-family:"Roboto Condensed",sans-serif}
.phone-bar__num{font-weight:900;font-size:38px;line-height:1}
.phone-bar__web{font-size:15px;letter-spacing:1px}
.phone-icon{width:34px;height:34px;border-radius:50%;background:var(--green);display:flex;align-items:center;justify-content:center;flex:none}
.contact-list{position:absolute;font-size:11px;color:var(--navy);line-height:1.9}
.contact-list span{display:inline-block;width:9px;height:9px;background:var(--green);border-radius:50%;margin-right:6px}
.follow{position:absolute;font-size:11px;font-weight:700;color:var(--navy)}
.follow i{display:inline-block;width:16px;height:16px;border-radius:50%;background:var(--green);margin-right:4px;margin-top:4px}
.back-band{position:absolute;left:0;top:18px;width:440px;height:68px;background:var(--green);clip-path:polygon(0 0,100% 0,94% 100%,0 100%);color:var(--white);font-family:"Roboto Condensed",sans-serif;font-weight:900;font-size:25px;line-height:1.08;padding:8px 18px}
.services{position:absolute;left:22px;top:100px;width:400px;display:grid;grid-template-columns:1fr 1fr;gap:16px 22px}
.service__icon{width:22px;height:22px;border:2px solid var(--navy);border-radius:4px;margin-bottom:4px}
.service__title{font-family:"Roboto Condensed",sans-serif;font-weight:900;font-size:17px;color:var(--green-dark)}
.service__text{font-size:10.5px;color:var(--text-grey);line-height:1.35}
.perks{position:absolute;left:22px;top:282px;list-style:none;font-family:"Roboto Condensed",sans-serif;font-weight:700;font-size:15px;color:var(--navy);line-height:1.45}
.perks li::before{content:"";display:inline-block;width:10px;height:10px;background:var(--green);margin-right:8px}
.address{position:absolute;left:468px;top:100px;font-size:11px;color:var(--text-grey);line-height:1.4}
.postage{position:absolute;right:18px;top:18px;width:82px;height:70px;border:1.5px solid #333;font-size:8px;font-weight:700;text-align:center;padding:6px 4px;line-height:1.35;color:#333}
</style>
</head>
<body>
<main class="sheet">

  <!-- Front side -->
  <section class="card card--front">
    <svg class="bg-art" width="801" height="494" viewBox="0 0 801 494">
      <defs>
        <linearGradient id="photoTone" x1="0" y1="0" x2="1" y2="1">
          <stop offset="0" stop-color="#cfd6dc"/>
          <stop offset=".5" stop-color="#8fa0b1"/>
          <stop offset="1" stop-color="#3f5674"/>
        </linearGradient>
      </defs>
      <path d="M330 0 H801 V400 H420 C395 300 360 200 330 0 Z" fill="url(#photoTone)" role="img" aria-label="Photo of a handyman repairing the plumbing under a kitchen sink"/>
      <path d="M300 0 C330 190 370 320 430 420" fill="none" stroke="var(--green)" stroke-width="14"/>
      <path d="M270 0 C300 170 340 300 398 420" fill="none" stroke="var(--navy)" stroke-width="4"/>
      <rect x="0" y="412" width="801" height="82" fill="#f4f4f4"/>
    </svg>

    <div class="brand" style="left:22px;top:22px;flex-direction:column;align-items:flex-start;gap:0">
      <div style="display:flex;align-items:center;gap:8px"><span class="brand__mark"></span><span class="brand__name">BRIGHTPATH</span></div>
      <div class="brand__tag">MAINTENANCE SERVICES</div>
    </div>

    <h1 class="headline">BrightPath<br>Makes Home<br>Maintenance<br>Easy</h1>
    <p class="subline">One Point of Contact For All Your<br>Property Maintenance Needs</p>

    <div class="seal" style="left:438px;top:300px;width:104px;height:104px"></div>

    <div class="cta-box" style="left:0;top:412px;width:190px;height:82px;padding:14px 16px">
      <small>WE ARE HERE TO HELP</small>
      <strong>REQUEST AN<br>FREE QUOTATION</strong>
    </div>
    <div class="phone-bar" style="left:190px;top:412px;width:330px;height:82px;padding:0 16px">
      <span class="phone-icon"><svg width="18" height="18" viewBox="0 0 24 24"><path fill="#fff" d="M6.6 10.8a15.1 15.1 0 0 0 6.6 6.6l2.2-2.2a1 1 0 0 1 1-.25 11.4 11.4 0 0 0 3.6.57 1 1 0 0 1 1 1V20a1 1 0 0 1-1 1A17 17 0 0 1 3 4a1 1 0 0 1 1-1h3.5a1 1 0 0 1 1 1c0 1.25.2 2.45.57 3.57a1 1 0 0 1-.25 1z"/></svg></span>
      <div><div class="phone-bar__num">555-214-7730</div><div class="phone-bar__web">www.brightpathpros.com</div></div>
    </div>
    <div class="contact-list" style="left:540px;top:426px">
      <div><span></span>info@brightpathpros.com</div>
      <div><span></span>www.brightpathpros.com</div>
    </div>
    <div class="follow" style="left:720px;top:424px">Follow Us<br><i></i><i></i></div>
  </section>
  <p class="side-label" style="top:576px">FRONT SIDE</p>

  <!-- Back side -->
  <section class="card card--back">
    <svg class="bg-art" width="801" height="481" viewBox="0 0 801 481">
      <path d="M448 0 C470 150 470 320 430 481" fill="none" stroke="var(--green)" stroke-width="5"/>
      <path d="M462 0 C484 150 484 320 444 481" fill="none" stroke="#d8e8c6" stroke-width="10"/>
    </svg>

    <div class="back-band">FOR ALL YOUR FACILITY<br>MAINTENANCE NEEDS</div>

    <div class="services">
      <div class="service"><div class="service__icon"></div><div class="service__title">PAINTING</div><div class="service__text">From small touch ups to full<br>makeovers, we have you covered!</div></div>
      <div class="service"><div class="service__icon"></div><div class="service__title">FLOORING REPAIR</div><div class="service__text">Need to replace or repair that<br>worn floor? Let us help!</div></div>
      <div class="service"><div class="service__icon"></div><div class="service__title">LIGHT PLUMBING</div><div class="service__text">We can help get rid of that leaky<br>faucet or clogged drain fast.</div></div>
      <div class="service"><div class="service__icon"></div><div class="service__title">PARKING LOT,<br>LIGHT REPAIR</div><div class="service__text">Need lot painting or new<br>exterior lighting? Contact us.</div></div>
    </div>

    <ul class="perks">
      <li>PROMPT SERVICES</li>
      <li>HONEST PRICES</li>
      <li>ONE SOURCE FOR MULTIPLE TRADES</li>
      <li>RELIABLE &amp; VETTED TRADESMEN</li>
    </ul>

    <div class="cta-box" style="left:0;top:372px;width:440px;height:34px;padding:4px 20px"><strong style="font-size:23px">REQUEST A FREE QUOTATION</strong></div>
    <div class="phone-bar" style="left:0;top:406px;width:440px;height:75px;padding:0 20px">
      <span class="phone-icon"><svg width="18" height="18" viewBox="0 0 24 24"><path fill="#fff" d="M6.6 10.8a15.1 15.1 0 0 0 6.6 6.6l2.2-2.2a1 1 0 0 1 1-.25 11.4 11.4 0 0 0 3.6.57 1 1 0 0 1 1 1V20a1 1 0 0 1-1 1A17 17 0 0 1 3 4a1 1 0 0 1 1-1h3.5a1 1 0 0 1 1 1c0 1.25.2 2.45.57 3.57a1 1 0 0 1-.25 1z"/></svg></span>
      <div><div class="phone-bar__num">555-214-7730</div><div class="phone-bar__web">www.brightpathpros.com</div></div>
    </div>

    <div class="seal" style="left:355px;top:318px;width:96px;height:96px"></div>

    <div class="brand" style="left:468px;top:48px;flex-direction:column;align-items:flex-start;gap:0">
      <div style="display:flex;align-items:center;gap:6px"><span class="brand__mark" style="width:20px;height:20px"></span><span class="brand__name" style="font-size:22px">BRIGHTPATH</span></div>
      <div class="brand__tag" style="font-size:8px;margin-left:26px">MAINTENANCE SERVICES</div>
    </div>
    <p class="address" style="top:98px">Your Company Address<br>Goes Here</p>
    <div class="postage">PRSRT STD<br>FIRST CLASS<br>U.S. POSTAGE<br>PAID<br>PERMIT 000</div>
  </section>
  <p class="side-label" style="top:1152px">BACK SIDE</p>

</main>
</body>
</html>
```